Enchilada sauce needs bright,delicious,appealing, attention-grabbing label

We are Brightfeather Kitchen LLC., and we need a label for a 20 oz. round jar w/ gold or black lid containing a most delicious and very hard to find Enchilada Sauce. The sauce itself is a deep, rich, dark red sauce in a glass container. The colors of the label should be the colors of sunset but also a pop of bright blue, yellow, white and black, maybe white letters for the name, which is ZOLTA and underneath, (enchilada salsa para muchos usos)

Your design will be on supermarket shelves across the USA and hopefully beyond, depends on how clever you are.                                   

should have chili peppers represented

```html
<!DOCTYPE html>
<html lang="en">
<head>
<meta charset="utf-8">
<title>ZOLTA Enchilada Sauce – Label Concepts</title>
<link rel="stylesheet" href="https://fonts.googleapis.com/css2?family=Arimo:wght@400&family=Cinzel:wght@500&family=Great+Vibes&family=Lobster&family=PT+Sans+Narrow&display=swap">
<style>
  :root {
    --page: #ffffff;
    --ink: #111111;
    --label-red: #d8202b;
    --label-red-light: #ef2b24;
    --rim-green: #7f9b3b;
    --rim-yellow: #f6e61c;
    --white: #ffffff;
    --flag-yellow: #f4ea2a;
    --script-gold: #e8b832;
    --subtitle-yellow: #f2e02b;
    --rule-gold: #f1cf3a;
    --ribbon-gold-dark: #a6741e;
    --ribbon-gold-light: #f2e08a;
    --ribbon-text: #d0202b;
    --art-red: #c91d22;
    --art-dark: #6a1a16;
    --art-orange: #f08a2a;
  }
  html, body {
    margin: 0;
    padding: 0;
    width: 1200px;
    height: 676px;
    overflow: hidden;
    background: var(--page);
  }
  .board {
    position: relative;
    width: 1200px;
    height: 676px;
  }
  .concept-title {
    position: absolute;
    top: 42px;
    margin: 0;
    font-family: "Arimo", Arial, sans-serif;
    font-weight: 400;
    font-size: 23px;
    letter-spacing: 0.5px;
    color: var(--ink);
  }
  .concept-title--previous { left: 38px; }
  .concept-title--revised { left: 560px; }
  .jar-label {
    position: absolute;
    top: 80px;
    width: 480px;
    height: 522px;
  }
  .jar-label--previous { left: 122px; }
  .jar-label--revised { left: 606px; }
  .flag-text {
    font-family: "Great Vibes", cursive;
    font-size: 28px;
    fill: var(--script-gold);
  }
  .brand-name {
    font-family: "Cinzel", serif;
    font-weight: 500;
    fill: var(--white);
  }
  .trademark {
    font-family: "Arimo", Arial, sans-serif;
    font-size: 15px;
    fill: var(--white);
  }
  .tagline {
    font-family: "PT Sans Narrow", "Arial Narrow", sans-serif;
    font-size: 21px;
    fill: var(--subtitle-yellow);
  }
  .maker-name {
    font-family: "Lobster", cursive;
    font-size: 20px;
    fill: var(--ribbon-text);
  }
  .net-weight {
    font-family: "Arimo", Arial, sans-serif;
    font-size: 13px;
    fill: var(--white);
  }
</style>
</head>
<body>
<main class="board">
  <h2 class="concept-title concept-title--previous">PREVIOUS C2</h2>
  <h2 class="concept-title concept-title--revised">REVISED C2</h2>

  <svg class="jar-label jar-label--previous" viewBox="0 0 480 522" aria-label="ZOLTA enchilada sauce label, previous concept">
    <defs>
      <linearGradient id="red-face-a" x1="0" x2="1" y1="0" y2="0">
        <stop offset="0" stop-color="var(--label-red)"/>
        <stop offset="0.5" stop-color="var(--label-red-light)"/>
        <stop offset="1" stop-color="var(--label-red)"/>
      </linearGradient>
      <linearGradient id="band-gold-a" x1="0" x2="1" y1="0" y2="0">
        <stop offset="0" stop-color="var(--ribbon-gold-light)"/>
        <stop offset="0.5" stop-color="var(--ribbon-gold-dark)"/>
        <stop offset="1" stop-color="var(--ribbon-gold-light)"/>
      </linearGradient>
      <radialGradient id="art-tone-a" cx="0.5" cy="0.5" r="0.6">
        <stop offset="0" stop-color="var(--art-orange)"/>
        <stop offset="0.45" stop-color="var(--art-red)"/>
        <stop offset="1" stop-color="var(--art-dark)"/>
      </radialGradient>
    </defs>
    <g class="label-rims">
      <ellipse cx="240" cy="261" rx="237" ry="258" fill="var(--label-red)"/>
      <ellipse cx="240" cy="261" rx="229" ry="250" fill="none" stroke="var(--rim-green)" stroke-width="4"/>
      <ellipse cx="240" cy="261" rx="223" ry="244" fill="none" stroke="var(--rim-green)" stroke-width="3"/>
      <ellipse cx="240" cy="261" rx="216" ry="237" fill="url(#red-face-a)"/>
      <ellipse cx="240" cy="261" rx="216" ry="237" fill="none" stroke="var(--white)" stroke-width="3"/>
    </g>
    <g class="top-flag">
      <polygon points="103,105 140,105 140,137 103,137 112,121" fill="var(--flag-yellow)"/>
      <polygon points="378,105 341,105 341,137 378,137 369,121" fill="var(--flag-yellow)"/>
      <text class="flag-text" x="240" y="131" text-anchor="middle">Enchilada Sauce</text>
    </g>
    <g class="divider">
      <line x1="72" y1="156" x2="408" y2="156" stroke="var(--rule-gold)" stroke-width="1.5"/>
      <circle cx="70" cy="156" r="2.5" fill="var(--rule-gold)"/>
      <circle cx="410" cy="156" r="2.5" fill="var(--rule-gold)"/>
    </g>
    <text class="brand-name" x="232" y="234" text-anchor="middle"><tspan font-size="84">Z</tspan><tspan font-size="74">OLTA</tspan></text>
    <text class="trademark" x="374" y="188">TM</text>
    <g class="divider">
      <line x1="72" y1="255" x2="408" y2="255" stroke="var(--rule-gold)" stroke-width="1.5"/>
      <circle cx="70" cy="255" r="2.5" fill="var(--rule-gold)"/>
      <circle cx="410" cy="255" r="2.5" fill="var(--rule-gold)"/>
    </g>
    <text class="tagline" x="240" y="283" text-anchor="middle">ENCHILADA SALSA PARA MUCHOS USOS</text>
    <rect x="86" y="314" width="308" height="50" fill="url(#band-gold-a)" role="img" aria-label="Gold ribbon banner carrying the maker name"/>
    <text class="maker-name" x="240" y="346" text-anchor="middle">Brightfeather Kitchen Llc</text>
    <rect x="172" y="366" width="136" height="76" rx="10" fill="url(#art-tone-a)" role="img" aria-label="Illustration of two crossed red chili peppers with a small flame"/>
    <text class="net-weight" x="240" y="467" text-anchor="middle">Net wt. 20oz.</text>
  </svg>

  <svg class="jar-label jar-label--revised" viewBox="0 0 480 522" aria-label="ZOLTA enchilada sauce label, revised concept">
    <defs>
      <linearGradient id="red-face-b" x1="0" x2="1" y1="0" y2="0">
        <stop offset="0" stop-color="var(--label-red)"/>
        <stop offset="0.5" stop-color="var(--label-red-light)"/>
        <stop offset="1" stop-color="var(--label-red)"/>
      </linearGradient>
      <linearGradient id="band-gold-b" x1="0" x2="1" y1="0" y2="0">
        <stop offset="0" stop-color="var(--ribbon-gold-light)"/>
        <stop offset="0.5" stop-color="var(--ribbon-gold-dark)"/>
        <stop offset="1" stop-color="var(--ribbon-gold-light)"/>
      </linearGradient>
      <radialGradient id="art-tone-b" cx="0.5" cy="0.5" r="0.6">
        <stop offset="0" stop-color="var(--art-orange)"/>
        <stop offset="0.45" stop-color="var(--art-red)"/>
        <stop offset="1" stop-color="var(--art-dark)"/>
      </radialGradient>
    </defs>
    <g class="label-rims">
      <ellipse cx="240" cy="261" rx="237" ry="258" fill="var(--label-red)"/>
      <ellipse cx="240" cy="261" rx="231" ry="252" fill="none" stroke="var(--rim-green)" stroke-width="4"/>
      <ellipse cx="240" cy="261" rx="226" ry="247" fill="none" stroke="var(--rim-yellow)" stroke-width="4"/>
      <ellipse cx="240" cy="261" rx="221" ry="242" fill="none" stroke="var(--rim-green)" stroke-width="3"/>
      <ellipse cx="240" cy="261" rx="213" ry="234" fill="url(#red-face-b)"/>
      <ellipse cx="240" cy="261" rx="213" ry="234" fill="none" stroke="var(--white)" stroke-width="3"/>
    </g>
    <g class="top-flag">
      <polygon points="103,105 140,105 140,137 103,137 112,121" fill="var(--flag-yellow)"/>
      <polygon points="378,105 341,105 341,137 378,137 369,121" fill="var(--flag-yellow)"/>
      <text class="flag-text" x="240" y="131" text-anchor="middle">Enchilada Sauce</text>
    </g>
    <g class="divider">
      <line x1="72" y1="156" x2="408" y2="156" stroke="var(--rule-gold)" stroke-width="1.5"/>
      <circle cx="70" cy="156" r="2.5" fill="var(--rule-gold)"/>
      <circle cx="410" cy="156" r="2.5" fill="var(--rule-gold)"/>
    </g>
    <text class="brand-name" x="232" y="234" text-anchor="middle"><tspan font-size="84">Z</tspan><tspan font-size="74">OLTA</tspan></text>
    <text class="trademark" x="374" y="188">TM</text>
    <g class="divider">
      <line x1="72" y1="255" x2="408" y2="255" stroke="var(--rule-gold)" stroke-width="1.5"/>
      <circle cx="70" cy="255" r="2.5" fill="var(--rule-gold)"/>
      <circle cx="410" cy="255" r="2.5" fill="var(--rule-gold)"/>
    </g>
    <text class="tagline" x="240" y="283" text-anchor="middle">ENCHILADA SALSA PARA MUCHOS USOS</text>
    <rect x="86" y="314" width="308" height="50" fill="url(#band-gold-b)" role="img" aria-label="Gold ribbon banner carrying the maker name"/>
    <text class="maker-name" x="240" y="346" text-anchor="middle">Brightfeather Kitchen Llc</text>
    <rect x="172" y="366" width="136" height="76" rx="10" fill="url(#art-tone-b)" role="img" aria-label="Illustration of two crossed red chili peppers with a small flame"/>
    <text class="net-weight" x="240" y="467" text-anchor="middle">Net wt. 20oz.</text>
  </svg>
</main>
</body>
</html>
```